Voltarey - Flyer design

Description -
Motorhome and Caravan EWOFs
Recreational Vehicles (such as caravans, motorhomes, RVs, Boats etc) and Relocatable buildings that can be connected to an electricity supply must be regularly checked for electrical safety. An EWOF needs to be issued every 4 years.
Pre-purchase house inspections
A pre-purchase electrical inspection prior to buying a home can be used to identify any dangerous and unsafe electrical parts of the installation that may be costly to repair once the property has been purchased. Giving you peace of mind when buying your new home.
High risk Electrical inspections
All Prescribed Electrical Work that falls under the High Risk category must be inspected by a Registered Electrical Inspector and have a Record of Inspection certificate issued.
Electric Vehicle Chargers
Any electrical vehicle charger that can be accessed by the public (ie in a non-domestic situation) must be periodically inspected and certified every 12 months.
General Electrical Services
Domestic and commercial - We do new builds, Renovations, Maintenance and more!
Dean Fowler - Electrician and Electrical Inspector
Ph - 0227839152
Dean@voltarey.co.nz
Auckland
------
I also want there to be a few symbols similar to the files I have attached.
The main areas that I am hoping to find work is with caravans/motohomes and EV car chargers so these symbols are quite important.
Thanks so much

```html
<!DOCTYPE html>
<html lang="en">
<head>
<meta charset="utf-8">
<title>Voltarey – Flyer</title>
<link href="https://fonts.googleapis.com/css2?family=Montserrat:wght@400;500;600;700;800&display=swap" rel="stylesheet">
<style>
  :root{
    --green:#8cc63f;
    --ink:#555759;
    --dark:#4a4a4c;
    --band:#626264;
    --paper:#ffffff;
    --stage:#cfcfcf;
    --photo-top:#e8dcd2;
    --photo-bottom:#cfa46a;
  }
  *{margin:0;padding:0;box-sizing:border-box}
  html,body{width:1200px;height:2253px;overflow:hidden;background:var(--stage)}
  body{font-family:'Montserrat',sans-serif;color:var(--ink);position:relative}
  .flyer{position:absolute;left:40px;top:335px;width:1120px;height:1583px;background:var(--paper);overflow:hidden}
  .flyer > *{position:absolute}

  .brand{left:744px;top:92px;display:flex;align-items:center;gap:16px}
  .brand-mark{width:30px;height:30px;background:var(--green)}
  .brand-name{font-size:50px;font-weight:500;color:var(--dark);letter-spacing:-0.5px;line-height:1}

  .portrait-frame{left:43px;top:227px;width:538px;height:537px;border:9px solid var(--green);border-right:none}
  .frame-right-top{left:572px;top:227px;width:9px;height:199px;background:var(--green)}
  .frame-right-bottom{left:572px;top:580px;width:9px;height:184px;background:var(--green)}
  .portrait{left:166px;top:68px;width:300px;height:687px;background:linear-gradient(180deg,var(--photo-top) 0%,var(--photo-bottom) 100%)}

  .name-bar{left:605px;width:474px;height:102px;background:var(--green);color:#fff;font-weight:800;font-size:96px;line-height:102px;padding-left:28px;letter-spacing:-1px;white-space:nowrap;overflow:hidden}
  .name-first{top:334px}
  .name-last{top:447px;font-size:86px}
  .role{left:607px;top:570px;font-size:41px;font-weight:500;line-height:50px;color:var(--ink)}
  .role-rule{left:611px;top:688px;width:153px;height:5px;background:var(--green)}

  .service{width:476px}
  .service-icon{position:absolute;left:0;top:0;width:102px;height:102px}
  .service-title{position:absolute;left:115px;top:14px;font-size:27px;font-weight:700;color:var(--green);line-height:31px;white-space:nowrap}
  .service-title::after{content:"";display:block;width:155px;height:4px;background:var(--green);margin-top:10px}
  .service-text{position:absolute;left:0;top:117px;width:476px;font-size:16.6px;line-height:20.6px;text-align:justify;color:var(--ink);letter-spacing:-0.1px}
  .svc-ewof{left:43px;top:822px}
  .svc-prepurchase{left:604px;top:822px}
  .svc-highrisk{left:47px;top:1076px}
  .svc-ev{left:604px;top:1076px}
  .svc-general{left:43px;top:1311px}

  .cta-bracket{left:604px;top:1370px;width:90px;height:68px;border:2px solid var(--green);border-right:none}
  .cta-pill{left:692px;top:1350px;width:383px;height:42px;border-radius:21px;background:var(--green);color:#fff;font-weight:800;font-size:33px;line-height:42px;text-align:center;letter-spacing:.5px}
  .cta-phone{left:692px;top:1398px;display:flex;align-items:center;gap:10px;font-size:54px;font-weight:800;color:var(--dark);letter-spacing:-1px}

  .footer{left:0;top:1495px;width:1120px;height:59px;background:var(--band);color:#fff}
  .footer-email{position:absolute;left:94px;top:0;height:59px;display:flex;align-items:center;gap:14px;font-size:33px;font-weight:500}
  .footer-city{position:absolute;left:797px;top:8px;height:43px;border-left:7px solid var(--green);padding-left:14px;font-size:33px;font-weight:700;line-height:43px}
</style>
</head>
<body>
<main class="flyer">
  <div class="brand"><span class="brand-mark"></span><span class="brand-name">Voltarey</span></div>

  <div class="portrait-frame"></div>
  <div class="frame-right-top"></div>
  <div class="frame-right-bottom"></div>
  <div class="portrait" role="img" aria-label="Photo of an electrician in a yellow hard hat, checked shirt and tool belt, arms crossed"></div>

  <div class="name-bar name-first">DEAN</div>
  <div class="name-bar name-last">FOWLER</div>
  <p class="role">Electrician and<br>Electrical Inspector</p>
  <div class="role-rule"></div>

  <section class="service svc-ewof">
    <svg class="service-icon" viewBox="0 0 102 102" fill="none" stroke="#555759" stroke-width="2.4" stroke-linejoin="round">
      <circle cx="51" cy="51" r="49" stroke="#8cc63f" stroke-width="2"/>
      <path d="M22 36h44a8 8 0 0 1 8 8v20H22z"/><path d="M74 64h8"/><rect x="28" y="43" width="14" height="9"/><rect x="56" y="43" width="10" height="21"/><circle cx="38" cy="68" r="5"/><path d="M22 58h28"/>
    </svg>
    <h2 class="service-title">Motorhome and<br>Caravan EWOFs</h2>
    <p class="service-text">Recreational Vehicles (such as caravans, motorhomes, RVs, Boats etc) and Relocatable buildings that can be connected to an electricity supply must be regularly checked for electrical safety. An EWOF needs to be issued every 4 years.</p>
  </section>

  <section class="service svc-prepurchase">
    <svg class="service-icon" viewBox="0 0 102 102" fill="none" stroke="#555759" stroke-width="2.4" stroke-linejoin="round">
      <circle cx="51" cy="51" r="49" stroke="#8cc63f" stroke-width="2"/>
      <path d="M20 48l28-22 28 22"/><path d="M27 44v28h20"/><circle cx="60" cy="62" r="10"/><path d="M67 69l9 9"/><path d="M62 34v-7h6v12"/>
    </svg>
    <h2 class="service-title">Pre-purchase<br>house inspections</h2>
    <p class="service-text">A pre-purchase electrical inspection prior to buying a home can be used to identify any dangerous and unsafe electrical parts of the installation that may be costly to repair once the property has been purchased. Giving you peace of mind when buying your new home.</p>
  </section>

  <section class="service svc-highrisk">
    <svg class="service-icon" viewBox="0 0 102 102" fill="none" stroke="#555759" stroke-width="2.4" stroke-linejoin="round">
      <circle cx="51" cy="51" r="49" stroke="#8cc63f" stroke-width="2"/>
      <path d="M51 22l24 9v18c0 15-10 25-24 31-14-6-24-16-24-31V31z"/><path d="M54 36l-10 16h9l-4 14 11-18h-9z"/>
    </svg>
    <h2 class="service-title">High risk<br>Electrical inspections</h2>
    <p class="service-text">All Prescribed Electrical Work that falls under the High Risk category must be inspected by a Registered Electrical Inspector and have a Record of Inspection certificate issued.</p>
  </section>

  <section class="service svc-ev">
    <svg class="service-icon" viewBox="0 0 102 102" fill="none" stroke="#555759" stroke-width="2.4" stroke-linejoin="round">
      <circle cx="51" cy="51" r="49" stroke="#8cc63f" stroke-width="2"/>
      <rect x="20" y="22" width="16" height="30" rx="2"/><path d="M36 30h6v14a6 6 0 0 0 12 0v-6"/><path d="M50 34h8v4h-8z"/><path d="M34 66l6-10h26l8 10v10H34z"/><circle cx="42" cy="76" r="4"/><circle cx="66" cy="76" r="4"/>
    </svg>
    <h2 class="service-title">Electric<br>Vehicle Chargers</h2>
    <p class="service-text">Any electrical vehicle charger that can be accessed by the public (ie in a non-domestic situation) must be periodically inspected and certified every 12 months.</p>
  </section>

  <section class="service svc-general">
    <svg class="service-icon" viewBox="0 0 102 102" fill="none" stroke="#555759" stroke-width="2.4" stroke-linejoin="round">
      <circle cx="51" cy="51" r="49" stroke="#8cc63f" stroke-width="2"/>
      <path d="M30 40a24 24 0 0 1 40-8"/><path d="M72 62a24 24 0 0 1-40 8"/><path d="M70 24v9h-9"/><path d="M32 78v-9h9"/><path d="M55 38l-10 14h9l-5 12 11-16h-9z"/>
    </svg>
    <h2 class="service-title">General<br>Electrical Services</h2>
    <p class="service-text">Domestic and commercial - We do new builds, Renovations, Maintenance and more!</p>
  </section>

  <div class="cta-bracket"></div>
  <div class="cta-pill">CALL US TODAY!</div>
  <div class="cta-phone">
    <svg width="44" height="44" viewBox="0 0 44 44"><circle cx="22" cy="22" r="22" fill="#8cc63f"/><path d="M15 11c2 0 3 4 3 5s-2 2-2 3c1 4 4 7 8 8 1 0 2-2 3-2s5 1 5 3-2 5-5 5c-8 0-17-9-17-17 0-3 3-5 5-5z" fill="#fff"/></svg>
    <span>0227839152</span>
  </div>

  <footer class="footer">
    <div class="footer-email">
      <svg width="34" height="24" viewBox="0 0 34 24"><rect width="34" height="24" fill="#8cc63f"/><path d="M1 1l16 13L33 1" fill="none" stroke="#626264" stroke-width="2"/></svg>
      <span>Dean@voltarey.co.nz</span>
    </div>
    <div class="footer-city">Auckland</div>
  </footer>
</main>
</body>
</html>
```